Design Challege - Simplify a Complex Message

We have a new website design, but one of the pages presents a particular problem.

Our company does ERP implementations. We have developed a proprietary approach to these implementations based on the idea that you must get eight (and only eight) things right. These eight things are listed below, summarized in one or two words each:

1. Value
2. Capability
3. Functionality
4. Data
5. Technology
6. Change Leadership
7. Quality
8. Governance

Each of these eight things can be summarized in a short paragraph, but when you combine all eight summaries with a brief introductory text, the result is a lot of text - so much text that the casual surfer may be overwhelmed by it.

The winning design will find an engaging way to present the information in a way that presents a high-level summary, using icons and one- or two-word descriptions above but revealing more information when clicked.

Our current design for this information, with a paragraph describing the eight elements in a table, is included as an upload in PDF and Microsoft Word formats. We are looking for a creative way to display these eight things, showing the detail only when the user wants to see it.

The website is being built in WordPress, using Elementor as a page builder.

We will implement (code) the page, but the winner will be asked to specify the widget or other add-in if one is required.

The design does not need to include a header or footer, we have those.

Target Market(s)

Business executives working in technology

Industry/Entity Type

Any

Number of Pages Required

1 page

Font styles to use
Sans Serif

Requirements
Must have
• A design for the body of the page, but not the header or footer.
Nice to have
• Unique icons or images appropriate for each of the eight things.
Should not have
• A lot of text on one page

```html
<!DOCTYPE html>
<html lang="en">
<head>
<meta charset="utf-8">
<title>ERP Implementations — Eight Things to Get Right</title>
<link rel="stylesheet" href="https://fonts.googleapis.com/css2?family=Montserrat:wght@700;800;900&family=Figtree:wght@400;500;700&display=swap">
<style>
  :root {
    --ink: #111111;
    --paper: #ffffff;
    --ground-light: #f7f7f7;
    --ground-mid: #e9e9e9;
    --slate: #577a87;
    --teal: #03adb0;
    --text-dark: #1e1e1e;
    --text-muted: #4a4a4a;
    --line: #1a1a1a;
  }
  * { margin: 0; padding: 0; box-sizing: border-box; }
  html, body { width: 1200px; height: 2431px; overflow: hidden; }
  body {
    position: relative;
    background: var(--ground-light);
    font-family: "Figtree", sans-serif;
    color: var(--text-dark);
  }
  .page-texture {
    position: absolute; left: 0; top: 342px; width: 1200px; height: 2089px;
    background:
      linear-gradient(90deg, rgba(0,0,0,0.035) 0%, rgba(0,0,0,0) 18%, rgba(0,0,0,0.03) 36%, rgba(0,0,0,0) 55%, rgba(0,0,0,0.035) 74%, rgba(0,0,0,0) 90%, rgba(0,0,0,0.03) 100%),
      linear-gradient(180deg, var(--ground-mid) 0%, var(--ground-light) 50%, var(--ground-mid) 100%);
  }
  .hero {
    position: absolute; left: 0; top: 0; width: 1200px; height: 342px;
    background: var(--ink);
  }
  .hero-title {
    position: absolute; left: 0; right: 0; top: 136px;
    text-align: center; color: var(--paper);
    font-family: "Montserrat", sans-serif; font-weight: 900; font-size: 51px;
    line-height: 60px;
  }
  .intro {
    position: absolute; left: 115px; top: 255px; width: 969px; height: 176px;
    background: var(--paper);
    box-shadow: 0 2px 6px rgba(0,0,0,0.12);
    padding: 34px 30px 0 32px;
  }
  .intro-title {
    text-align: center; font-weight: 700; font-size: 25px; color: var(--ink);
    margin-bottom: 13px;
  }
  .intro-text { font-size: 17px; line-height: 21.5px; letter-spacing: 0.2px; color: var(--text-muted); }
  .card {
    position: absolute; width: 445px; height: 325px; border-radius: 6px;
    color: var(--paper); padding: 128px 48px 0 35px;
  }
  .card--slate { background: var(--slate); }
  .card--teal { background: var(--teal); }
  .card--lifted { box-shadow: 0 8px 16px rgba(0,0,0,0.25); }
  .card-badge {
    position: absolute; left: 140px; top: -82px; width: 164px; height: 164px;
    border-radius: 50%; background: var(--paper);
    display: flex; align-items: center; justify-content: center;
    box-shadow: 0 1px 4px rgba(0,0,0,0.08);
  }
  .card-badge svg { width: 72px; height: 72px; fill: none; stroke: var(--line); stroke-width: 2; stroke-linecap: round; stroke-linejoin: round; }
  .card-details summary { list-style: none; cursor: pointer; }
  .card-details summary::-webkit-details-marker { display: none; }
  .card-title { font-family: "Montserrat", sans-serif; font-weight: 800; font-size: 20px; line-height: 24px; margin-bottom: 7px; }
  .card-text { font-size: 14px; line-height: 17px; letter-spacing: 0.1px; }
  .card-list { list-style: none; padding-left: 21px; }
  .card-list li { position: relative; }
  .card-list li::before { content: "•"; position: absolute; left: -13px; }
  .card-link { display: inline-block; margin-top: 7px; font-family: "Montserrat", sans-serif; font-weight: 800; font-size: 13px; color: var(--paper); text-decoration: none; }
  .card-link--plain { font-family: "Figtree", sans-serif; font-weight: 400; font-size: 14px; }
  .col-left { left: 133px; }
  .col-right { left: 622px; }
  .row-1 { top: 567px; }
  .row-2 { top: 1028px; }
  .row-3 { top: 1489px; }
  .row-4 { top: 1950px; }
</style>
</head>
<body>
  <div class="page-texture" role="img" aria-label="Light grey speckled paper texture background"></div>

  <header class="hero">
    <h1 class="hero-title">ERP Implementations</h1>
  </header>

  <section class="intro">
    <h2 class="intro-title">Eight Things to Get Right</h2>
    <p class="intro-text">Like the roots and branches of a tree, there are many considerations in an ERP implementation. Focus too much on the minor details, and you can lose sight of the tree. In an ERP implementation, you must get eight major things right to be successful. Ignore any of them, and your implementation will fail. Get them right, and you will likely succeed.</p>
  </section>

  <article class="card card--slate card--lifted col-left row-1">
    <div class="card-badge">
      <svg viewBox="0 0 72 72"><rect x="6" y="56" width="6" height="8"/><rect x="15" y="52" width="6" height="12"/><rect x="24" y="48" width="6" height="16"/><rect x="33" y="44" width="6" height="20"/><rect x="42" y="38" width="6" height="26"/><rect x="51" y="30" width="6" height="34"/><rect x="60" y="22" width="6" height="42"/><polyline points="6,48 30,32 44,34 64,12"/><polyline points="56,12 64,12 64,20"/><circle cx="28" cy="20" r="9"/><path d="M31 16h-4a2 2 0 0 0 0 4h2a2 2 0 0 1 0 4h-4M28 14v12"/></svg>
    </div>
    <details class="card-details" open>
      <summary><h3 class="card-title">Value</h3></summary>
      <p class="card-text">The project must provide value that significantly exceeds potential project costs and should be aligned with the company’s strategy. Its value and strategic alignment must be part of a vision shared by the company’s leadership. Value from the project must be delivered in a way that respects resource constraints.</p>
      <a class="card-link" href="#value">Learn More</a>
    </details>
  </article>

  <article class="card card--teal col-right row-1">
    <div class="card-badge">
      <svg viewBox="0 0 72 72"><path d="M36 12a16 16 0 0 0-10 28c3 3 4 6 4 9h12c0-3 1-6 4-9a16 16 0 0 0-10-28z"/><path d="M36 12v37"/><path d="M28 22c3 0 4 3 4 5M27 32c3-1 6 1 6 3"/><rect x="30" y="52" width="12" height="4"/><rect x="31" y="58" width="10" height="4"/><path d="M36 2v5M54 20h6M50 8l-3 3M50 32l3 3"/></svg>
    </div>
    <details class="card-details" open>
      <summary><h3 class="card-title">Capability</h3></summary>
      <div class="card-text">
        <p>The company and the implementation team must be capable of implementing the project on their own or with help. The project must have the following:</p>
        <ul class="card-list">
          <li>Resources required, including people, time, and budget.</li>
          <li>Processes required, usually delivered through a comprehensive methodology.</li>
        </ul>
      </div>
      <a class="card-link" href="#capability">Learn More</a>
    </details>
  </article>

  <article class="card card--teal col-left row-2">
    <div class="card-badge">
      <svg viewBox="0 0 72 72"><circle cx="38" cy="34" r="14"/><circle cx="38" cy="34" r="9"/><circle cx="38" cy="34" r="4"/><circle cx="14" cy="14" r="8"/><polyline points="10,14 13,17 18,11"/><circle cx="60" cy="60" r="8"/><polyline points="56,60 59,63 64,57"/><rect x="54" y="8" width="4" height="10"/><rect x="60" y="4" width="4" height="14"/><rect x="48" y="12" width="4" height="6"/><rect x="6" y="50" width="18" height="14"/><path d="M10 55h10M10 59h6"/><path d="M30 48l4 14h8l4-14"/></svg>
    </div>
    <details class="card-details" open>
      <summary><h3 class="card-title">Functionality</h3></summary>
      <p class="card-text">An ERP project must support required business processes, both now and in the future. A systematic review of all business processes and how they will be supported, either by the system or otherwise, is crucial.</p>
      <a class="card-link" href="#functionality">Learn More</a>
    </details>
  </article>

  <article class="card card--slate col-right row-2">
    <div class="card-badge">
      <svg viewBox="0 0 72 72"><ellipse cx="36" cy="14" rx="26" ry="7"/><path d="M10 14v44c0 4 12 7 26 7s26-3 26-7V14"/><path d="M10 25c0 4 12 7 26 7s26-3 26-7M10 36c0 4 12 7 26 7s26-3 26-7M10 47c0 4 12 7 26 7s26-3 26-7"/><path d="M14 18v6M14 30v6M14 41v6M14 52v6"/></svg>
    </div>
    <details class="card-details" open>
      <summary><h3 class="card-title">Data</h3></summary>
      <p class="card-text">ERP systems are data-hungry creatures. Please be careful before assuming that because so much data goes into them, an equal amount of insight will emerge. Getting data right means considering data architecture, migration, integration, governance, and, perhaps most importantly, access.</p>
      <a class="card-link" href="#data">Learn More</a>
    </details>
  </article>

  <article class="card card--slate col-left row-3">
    <div class="card-badge">
      <svg viewBox="0 0 72 72"><path d="M36 6v8l-6 2-5-5-6 6 4 6-2 6h-8v10h8l2 6-4 6 6 6 5-5 6 2v8"/><path d="M36 22a14 14 0 0 0 0 28"/><path d="M36 28h10l4-6h8M36 36h20M36 44h10l4 6h8"/><circle cx="60" cy="22" r="3"/><circle cx="60" cy="36" r="3"/><circle cx="60" cy="50" r="3"/></svg>
    </div>
    <details class="card-details" open>
      <summary><h3 class="card-title">Technology</h3></summary>
      <p class="card-text">What is the platform for the system? Is it offered by a vendor that will be around for as long as your system? Will it integrate with your other systems? Are resources available to support it? Can you change it without painting yourself into a corner? Will your technology scale as you grow?</p>
      <a class="card-link" href="#technology">Learn More</a>
    </details>
  </article>

  <article class="card card--teal col-right row-3">
    <div class="card-badge">
      <svg viewBox="0 0 72 72"><path d="M36 4l2 4 4 1-3 3 1 4-4-2-4 2 1-4-3-3 4-1z"/><circle cx="36" cy="24" r="5"/><path d="M28 46v-8a8 8 0 0 1 16 0v8"/><path d="M20 22l-4-2M20 32h-6M52 22l4-2M52 32h6"/><circle cx="14" cy="52" r="4"/><circle cx="26" cy="52" r="4"/><circle cx="36" cy="50" r="4"/><circle cx="46" cy="52" r="4"/><circle cx="58" cy="52" r="4"/><path d="M8 64v-2a6 6 0 0 1 12 0v2zM20 64v-2a6 6 0 0 1 12 0v2zM30 64v-4a6 6 0 0 1 12 0v4zM40 64v-2a6 6 0 0 1 12 0v2zM52 64v-2a6 6 0 0 1 12 0v2z"/></svg>
    </div>
    <details class="card-details" open>
      <summary><h3 class="card-title">Change Leadership</h3></summary>
      <p class="card-text">Change leadership (often called change management) considers the human side of an ERP implementation. Change is hard, even if it’s a good change. Training is an important element of change leadership. But beyond training, consideration must be given to the people using the system.</p>
      <a class="card-link card-link--plain" href="#change-leadership">Learn More</a>
    </details>
  </article>

  <article class="card card--teal col-left row-4">
    <div class="card-badge">
      <svg viewBox="0 0 72 72"><path d="M36 4l7 5 9-1 4 8 8 4-1 9 5 7-5 7 1 9-8 4-4 8-9-1-7 5-7-5-9 1-4-8-8-4 1-9-5-7 5-7-1-9 8-4 4-8 9 1z"/><circle cx="36" cy="36" r="18"/><polyline points="28,36 34,42 45,30"/></svg>
    </div>
    <details class="card-details" open>
      <summary><h3 class="card-title">Quality</h3></summary>
      <p class="card-text">Quality is multi-dimensional, and it’s more than a measurement; it’s a perception. An ERP needs to be reliable. But poor performance or poor user experience are often root causes of implementation failure. Take an approach to quality that starts with perceptions and considers all aspects of quality.</p>
      <a class="card-link" href="#quality">Learn More</a>
    </details>
  </article>

  <article class="card card--slate col-right row-4">
    <div class="card-badge">
      <svg viewBox="0 0 72 72"><path d="M32 4h8l1 7 6 2 5-4 6 6-4 5 2 6 7 1v8l-7 1-2 6 4 5-6 6-5-4-6 2-1 7h-8l-1-7-6-2-5 4-6-6 4-5-2-6-7-1v-8l7-1 2-6-4-5 6-6 5 4 6-2z"/><circle cx="36" cy="36" r="18"/><path d="M24 30l12-8 12 8zM26 46h20M27 33v10M33 33v10M39 33v10M45 33v10"/></svg>
    </div>
    <details class="card-details" open>
      <summary><h3 class="card-title">Governance</h3></summary>
      <p class="card-text">ERP projects require both management and leadership. Planning, changing plans, communication, decision making, and guidance are critical aspects of management. But without the leadership qualities of motivating a team, setting clear goals, and using influence to reach goals, even well-managed projects can fail.</p>
      <a class="card-link" href="#governance">Learn More</a>
    </details>
  </article>
</body>
</html>
```